Powerpoint design for Summit Lane Advisors

We would like to have a Power point template/design with flexibilities and good opportunities to do changes.
• Be able to change in image background
• Themes are SLA colors and complementary colors. Please come with suggestions.
• Alternate white and blue background
• Standard functions and opportunities within Powerpoint should be able to be used or be accessible.
• Feel free to change/alter the logo for example remove or separate the text in the logo ("Summit Lane Advisors" ) and the tagline ("Clear paths to lasting growth")
• www.summitlaneadvisors.se

```html
<!DOCTYPE html>
<html lang="en">
<head>
<meta charset="utf-8">
<title>Summit Lane Advisors – Presentation Template</title>
<link href="https://fonts.googleapis.com/css2?family=Roboto:wght@300;400;500;700&display=swap" rel="stylesheet">
<style>
:root{
  --navy:#0f3b73;
  --navy-deep:#0b3063;
  --band:#2e5d9b;
  --blue:#2d67b3;
  --sky:#4d8fd6;
  --red:#a31d23;
  --gray:#7c7d80;
  --gray-dark:#5f6165;
  --paper:#ffffff;
  --mist:#eef1f6;
  --ink:#3a4556;
  --soft:#c9d3e0;
}
*{box-sizing:border-box;margin:0;padding:0}
html,body{width:926px;height:1200px;overflow:hidden}
body{
  position:relative;
  font-family:'Roboto',Arial,sans-serif;
  background:radial-gradient(ellipse 70% 45% at 100% 0%,#9b9b9b 0%,#d3d3d3 40%,#ffffff 100%);
  color:var(--ink);
}
svg.defs{position:absolute;width:0;height:0}

/* Brand header */
.brand{position:absolute;top:14px;left:0;width:926px;text-align:center;color:var(--navy)}
.brand-mark{font-weight:500;font-size:60px;line-height:66px;letter-spacing:1px}
.brand-name{font-weight:500;font-size:21px;line-height:24px;margin-top:2px}
.brand-tagline{font-weight:400;font-size:11px;letter-spacing:3.4px;margin-top:6px}

/* Slide grid */
.slide{position:absolute;width:238px;height:134px;overflow:hidden;background:var(--paper);box-shadow:0 6px 14px rgba(0,0,0,.28)}
.c1{left:54px}.c2{left:344px}.c3{left:634px}
.r1{top:144px}.r2{top:296px}.r3{top:448px}.r4{top:600px}.r5{top:751px}.r6{top:903px}.r7{top:1055px}
.navy{background:var(--navy);color:#fff}
.abs{position:absolute}
.ph{position:absolute}
.ph-tech{background:linear-gradient(135deg,#dfe8f2 0%,#93acc9 55%,#4e6f98 100%)}
.ph-dark{background:linear-gradient(135deg,#2f333b 0%,#6c717a 60%,#a9adb4 100%)}
.ph-warm{background:linear-gradient(135deg,#e9e4dc 0%,#b8b0a4 50%,#6d6760 100%)}
.ph-chart{background:linear-gradient(135deg,#e9f2fb 0%,#8fbde8 50%,#2f7bc7 100%)}
.ph-glow{background:linear-gradient(135deg,#1d1a18 0%,#5b4630 50%,#c4a06a 100%)}
.ph-map{background:linear-gradient(135deg,#e7ebf0 0%,#b6c1cf 60%,#8693a4 100%)}
.ph-studio{background:linear-gradient(135deg,#2a2540 0%,#6a5a9a 50%,#c9a7d6 100%)}

/* Slide furniture */
.mark{position:absolute;top:5px;right:13px;font-weight:500;font-size:8px;color:var(--navy);letter-spacing:.3px}
.navy .mark,.mark.light{color:#fff}
.foot{position:absolute;left:14px;right:14px;bottom:6px;display:flex;justify-content:space-between;font-size:3.2px;color:#5a6272}
.navy .foot,.foot.light{color:#cfd9e8}
.foot i{font-style:normal;font-size:2.4px}
.title{font-weight:400;font-size:5.6px;line-height:1.2}
.sub{font-size:2.6px;line-height:1.4}
.lo{font-size:2.2px;line-height:1.4;color:inherit;opacity:.85}
.lbl{font-size:3.6px;line-height:1.2}
.red-t{color:var(--red)}
.navy-t{color:var(--navy)}
.center{text-align:center}
ul.bul{list-style:none;font-size:3px;line-height:1.25}
ul.bul li{position:relative;padding-left:4px;margin-bottom:1.4px}
ul.bul li::before{content:"";position:absolute;left:0;top:1.1px;width:1.2px;height:1.2px;border-radius:50%;background:currentColor}

/* Icons */
.dot{position:absolute;border-radius:50%;display:flex;align-items:center;justify-content:center;color:#fff}
.dot svg{width:55%;height:55%}
.dot.gray{background:var(--gray)}
.dot.red{background:var(--red)}
.dot.blue{background:var(--blue)}
.dot.ring{box-shadow:0 0 0 1.2px rgba(255,255,255,.45)}
.ico{width:6px;height:6px;color:#fff}
svg use{fill:none;stroke:currentColor}

/* Hero slides */
.hero-mark{position:absolute;font-weight:500;font-size:32px;color:#e7ebf1;letter-spacing:1px}
.hero-name{position:absolute;font-size:8.6px;color:#fff;font-weight:400}
.hero-name small{display:block;font-size:4.6px;letter-spacing:.6px;text-align:center;color:#d6e0ee}

/* Numbers */
.stat{position:absolute;top:48px;width:60px;text-align:center}
.stat b{display:block;font-weight:500;font-size:10px}
.stat span{display:block;font-size:3.8px;margin:2px 0 3px}

/* Boxes */
.box{position:absolute;width:47px;height:42px;padding:4px 3px;text-align:center;color:#fff}
.box .ico{display:block;margin:2px auto 6px}
.box .lbl{font-size:3.2px;margin-bottom:2px}
.num{font-weight:700;font-size:8px;color:var(--navy)}
.card{position:absolute;top:29px;width:47px;height:87px;text-align:center;padding:9px 4px 0}
.card .price{font-weight:300;font-size:15px;line-height:1}
.card .price small{font-size:4px}
.card .tier{font-weight:700;font-size:3.1px;margin:10px 0 3px}
.card .btn{margin:4px auto 0;width:18px;height:3.4px;border-radius:2px;font-size:1.8px;line-height:3.4px}
</style>
</head>
<body>

<svg class="defs" aria-hidden="true">
  <symbol id="i-pie" viewBox="0 0 24 24"><circle cx="12" cy="12" r="9" stroke-width="2"/><path d="M12 12V3M12 12h9" stroke-width="2"/><path d="M12 12V4a8 8 0 0 1 8 8z" fill="currentColor"/></symbol>
  <symbol id="i-hour" viewBox="0 0 24 24"><path d="M6 3h12M6 21h12M8 3c0 6 8 5 8 9s-8 3-8 9M16 3c0 6-8 5-8 9s8 3 8 9" stroke-width="2"/></symbol>
  <symbol id="i-target" viewBox="0 0 24 24"><circle cx="12" cy="12" r="9" stroke-width="2"/><circle cx="12" cy="12" r="5" stroke-width="2"/><circle cx="12" cy="12" r="1.5" stroke-width="2"/></symbol>
  <symbol id="i-globe" viewBox="0 0 24 24"><circle cx="12" cy="12" r="9" stroke-width="2"/><ellipse cx="12" cy="12" rx="4" ry="9" stroke-width="2"/><path d="M3 12h18" stroke-width="2"/></symbol>
  <symbol id="i-people" viewBox="0 0 24 24"><circle cx="12" cy="7" r="3.5" stroke-width="2"/><circle cx="7" cy="15" r="3.5" stroke-width="2"/><circle cx="17" cy="15" r="3.5" stroke-width="2"/></symbol>
  <symbol id="i-gauge" viewBox="0 0 24 24"><path d="M3 17a9 9 0 0 1 18 0" stroke-width="2"/><path d="M12 17l5-6" stroke-width="2"/></symbol>
  <symbol id="i-cal" viewBox="0 0 24 24"><rect x="4" y="5" width="16" height="15" rx="1" stroke-width="2"/><path d="M4 10h16M8 3v4M16 3v4" stroke-width="2"/></symbol>
  <symbol id="i-board" viewBox="0 0 24 24"><rect x="3" y="4" width="18" height="12" stroke-width="2"/><path d="M12 16v5M8 21h8M7 12l3-3 3 2 4-4" stroke-width="2"/></symbol>
  <symbol id="i-bank" viewBox="0 0 24 24"><path d="M3 9l9-5 9 5M5 10v8M10 10v8M14 10v8M19 10v8M3 20h18" stroke-width="2"/></symbol>
  <symbol id="i-search" viewBox="0 0 24 24"><circle cx="10" cy="10" r="6" stroke-width="2"/><path d="M15 15l6 6" stroke-width="2"/></symbol>
  <symbol id="i-send" viewBox="0 0 24 24"><path d="M3 11l18-8-8 18-2-8z" stroke-width="2"/></symbol>
  <symbol id="i-user" viewBox="0 0 24 24"><circle cx="12" cy="12" r="9" stroke-width="2"/><circle cx="12" cy="10" r="3" stroke-width="2"/><path d="M6 18c2-3 10-3 12 0" stroke-width="2"/></symbol>
  <symbol id="i-image" viewBox="0 0 24 24"><rect x="3" y="4" width="18" height="16" stroke-width="2"/><path d="M3 17l6-6 5 5 3-3 4 4" stroke-width="2"/></symbol>
</svg>

<header class="brand">
  <div class="brand-mark">SLA</div>
  <div class="brand-name">Summit Lane Advisors</div>
  <div class="brand-tagline">Clear paths to lasting growth</div>
</header>

<!-- Row 1 -->
<section class="slide c1 r1 navy">
  <div class="ph" style="inset:0;background:linear-gradient(135deg,#25548e 0%,#103c74 55%,#0d3569 100%)" role="img" aria-label="Faded photo of a business desk with laptop and documents"></div>
  <div class="hero-mark" style="left:24px;top:46px">SLA</div>
  <div class="hero-name" style="left:125px;top:67px">Summit Lane Advisors<small>Clear paths to lasting digital growth</small></div>
</section>

<section class="slide c2 r1 navy">
  <div class="ph" style="inset:0;background:radial-gradient(ellipse at 55% 45%,#3c6aa3 0%,#174580 45%,#0f3b73 100%)" role="img" aria-label="Faded photo of a laptop keyboard in blue light"></div>
  <div class="hero-mark" style="left:24px;top:46px">SLA</div>
  <div class="hero-name" style="left:125px;top:67px">Summit Lane Advisors<small>Clear paths to lasting digital growth</small></div>
</section>

<section class="slide c3 r1 navy">
  <div class="mark">SLA</div>
  <div class="ph ph-dark" style="left:0;top:19px;width:119px;height:95px" role="img" aria-label="Photo of a hand touching a digital shopping interface"></div>
  <div class="abs" style="left:135px;top:23px;width:90px">
    <div style="font-weight:500;font-size:5.4px">Summit Lane Advisors</div>
    <div style="font-size:4px;margin-top:5px">Digital development and transformation</div>
    <div class="lo" style="font-size:3px;margin-top:5px">New tools keep reshaping how people work, how they talk to one another and how they compare, choose and buy what they need.</div>
    <div style="width:10px;height:.5px;background:#fff;margin:4px 0;opacity:.6"></div>
    <div class="lo">Buyers today arrive well prepared and make up their own minds. Every new channel opens room for fresh ideas and services.</div>
    <div class="lo" style="margin-top:3px">Firms that learn how their offer is found, judged and used across channels are better placed to meet each buyer where they are. Moving from guesswork to insight to action is the core of the work. Insight into current change gives leaders a firm base for choosing where to invest next.</div>
  </div>
  <div class="foot"><span>Clear paths to lasting digital growth</span><i>www.yourdomain.se &nbsp;|&nbsp; 3</i></div>
</section>

<!-- Row 2 -->
<section class="slide c1 r2">
  <div class="abs" style="left:13px;top:5px;font-weight:500;font-size:8px;color:var(--navy)">SLA</div>
  <div class="ph ph-map" style="left:119px;top:0;width:119px;height:134px" role="img" aria-label="World map with financial data overlay"></div>
  <div class="abs" style="left:13px;top:22px;width:100px">
    <div class="navy-t" style="font-weight:700;font-size:5.4px;line-height:1.2">Digital development and<br>transformation</div>
    <div class="red-t" style="font-size:4px;margin-top:7px">Our passion</div>
    <div class="lo">We love turning complex change into simple next steps, so each client can act early and stay ahead in its own market.</div>
    <div class="red-t" style="font-size:4px;margin-top:3px">Concept Development</div>
    <div class="lo">Side by side with each client we map goals, gaps and openings, then shape a clear concept with tools and working methods to match.</div>
    <div class="red-t" style="font-size:4px;margin-top:3px">Concept Implementation</div>
    <div class="lo">A good idea needs a sound rollout. We plan the steps, roles and timing together so the launch lands well.</div>
    <div class="red-t" style="font-size:4px;margin-top:3px">Analytics and evaluation</div>
    <div class="lo">We measure before, during and after each project, and feed what we learn back into the next round of ideas and delivery.</div>
  </div>
</section>

<section class="slide c2 r2">
  <div class="ph" style="left:0;top:0;width:238px;height:134px;background:linear-gradient(180deg,#f3f5f8 0%,#e2e7ee 100%)" role="img" aria-label="Faded photo of a person at a glass wall"></div>
  <div class="mark">SLA</div>
  <div class="abs title center navy-t" style="left:0;right:0;top:18px;letter-spacing:.3px">Summit Lane Advisors Services</div>
  <div class="abs sub center" style="left:0;right:0;top:31px">Lorem ipsum dolor sit amet, consectetur adipiscing elit, sed do eiusmod tempor incididunt ut labore et dolore magna</div>
  <div class="abs" style="left:0;top:40px;width:238px;height:56px;background:var(--navy)"></div>
  <div class="dot gray ring" style="left:35px;top:46px;width:14px;height:14px"><svg><use href="#i-pie"/></svg></div>
  <div class="dot blue ring" style="left:112px;top:46px;width:14px;height:14px"><svg><use href="#i-people"/></svg></div>
  <div class="dot red ring" style="left:187px;top:46px;width:14px;height:14px"><svg><use href="#i-hour"/></svg></div>
  <div class="abs center" style="left:14px;top:65px;width:58px;color:#fff"><div class="lbl">Your description text</div><div class="lo">Lorem ipsum dolor sit amet, consectetur adipiscing elit, sed do eiusmod tempor incididunt ut labore et dolore magna aliqua. Ut</div></div>
  <div class="abs center" style="left:90px;top:65px;width:58px;color:#fff"><div class="lbl">Your description text</div><div class="lo">Lorem ipsum dolor sit amet, consectetur adipiscing elit, sed do eiusmod tempor incididunt ut labore et dolore magna aliqua. Ut</div></div>
  <div class="abs center" style="left:165px;top:65px;width:58px;color:#fff"><div class="lbl">Your description text</div><div class="lo">Lorem ipsum dolor sit amet, consectetur adipiscing elit, sed do eiusmod tempor incididunt ut labore et dolore magna aliqua. Ut</div></div>
  <div class="abs navy-t" style="left:17px;top:98px;width:204px;font-size:3.2px;line-height:1.55;opacity:.85">Lorem ipsum dolor sit amet, consectetur adipiscing elit, sed do eiusmod tempor incididunt ut labore et dolore magna aliqua. Ut enim ad minim veniam, quis nostrud exercitation ullamco laboris nisi ut aliquip ex ea commodo consequat. Duis aute irure dolor in reprehenderit in voluptate velit esse cillum dolore eu fugiat nulla pariatur. Excepteur sint occaecat cupidatat non proident, sunt</div>
  <div class="foot"><span></span><i>www.yourdomain.se &nbsp;|&nbsp; 2</i></div>
</section>

<section class="slide c3 r2 navy">
  <div class="mark" style="left:13px;right:auto">SLA</div>
  <div class="ph ph-tech" style="left:164px;top:0;width:74px;height:134px" role="img" aria-label="Photo of a woman touching a digital glass wall"></div>
  <div class="abs title" style="left:15px;top:23px">Summit Lane Advisors Core Services</div>
  <div class="abs" style="left:14px;top:35px;width:65px"><svg class="ico"><use href="#i-pie"/></svg><div class="lbl" style="font-size:3.4px;margin:2px 0">Your description text</div><div class="lo">Lorem ipsum dolor sit amet, consectetur adipiscing elit, sed do eiusmod tempor incididunt ut labore et dolore magna aliqua. Ut enim ad minim veniam, quis nostrud exercitation ullamco laboris nisi ut aliquip ex ea commodo consequat. Duis aute irure dolor</div></div>
  <div class="abs" style="left:90px;top:35px;width:65px"><svg class="ico"><use href="#i-target"/></svg><div class="lbl" style="font-size:3.4px;margin:2px 0">Your description text</div><div class="lo">Lorem ipsum dolor sit amet, consectetur adipiscing elit, sed do eiusmod tempor incididunt ut labore et dolore magna aliqua. Ut enim ad minim veniam, quis nostrud exercitation ullamco laboris nisi ut aliquip ex ea commodo consequat. Duis aute irure dolor</div></div>
  <div class="abs" style="left:14px;top:80px;width:65px"><svg class="ico"><use href="#i-people"/></svg><div class="lbl" style="font-size:3.4px;margin:2px 0">Your description text</div><div class="lo">Lorem ipsum dolor sit amet, consectetur adipiscing elit, sed do eiusmod tempor incididunt ut labore et dolore magna aliqua. Ut enim ad minim veniam, quis nostrud exercitation ullamco laboris nisi ut aliquip ex ea commodo consequat. Duis aute irure dolor</div></div>
  <div class="abs" style="left:90px;top:80px;width:65px"><svg class="ico"><use href="#i-globe"/></svg><div class="lbl" style="font-size:3.4px;margin:2px 0">Your description text</div><div class="lo">Lorem ipsum dolor sit amet, consectetur adipiscing elit, sed do eiusmod tempor incididunt ut labore et dolore magna aliqua. Ut enim ad minim veniam, quis nostrud exercitation ullamco laboris nisi ut aliquip ex ea commodo consequat. Duis aute irure dolor</div></div>
  <div class="foot"><span>Clear paths to lasting digital growth</span><i>www.yourdomain.se &nbsp;|&nbsp; 19</i></div>
</section>

<!-- Row 3 -->
<section class="slide c1 r3 navy">
  <div class="mark">SLA</div>
  <div class="abs title center" style="left:0;right:0;top:26px">Summit Lane Advisors in Numbers</div>
  <div class="stat" style="left:30px"><b>1200k $</b><span>Income 2020</span><div class="lo">Lorem ipsum dolor sit amet, consectetur adipiscing elit, sed do eiusmod tempor incididunt ut labore et dolore magna aliqua.</div></div>
  <div class="stat" style="left:89px"><b>100%</b><span>Customer Satisfaction</span><div class="lo">Lorem ipsum dolor sit amet, consectetur adipiscing elit, sed do eiusmod tempor incididunt ut labore et dolore magna aliqua.</div></div>
  <div class="stat" style="left:155px"><b>3,610</b><span>Hours billed</span><div class="lo">Lorem ipsum dolor sit amet, consectetur adipiscing elit, sed do eiusmod tempor incididunt ut labore et dolore magna aliqua.</div></div>
  <div class="foot"><span>Clear paths to lasting digital growth</span><i>www.summitlaneadvisors.se &nbsp;|&nbsp; 7</i></div>
</section>

<section class="slide c2 r3">
  <div class="mark">SLA</div>
  <div class="abs title center navy-t" style="left:0;right:0;top:19px">Summit Lane Advisors in Numbers<br>Subtitle slide with comments</div>
  <div class="abs sub center" style="left:22px;right:22px;top:41px;line-height:1.7">Lorem ipsum dolor sit amet, consectetur adipiscing elit, sed do eiusmod tempor incididunt ut labore et dolore magna aliqua. Lorem ipsum dolor sit amet, consectetur adipiscing elit, sed do eiusmod tempor incididunt ut labore et dolore magna aliqua. Lorem ipsum dolor sit amet, consectetur adipiscing elit, sed do eiusmod tempor incididunt ut labore et</div>
  <div class="ph ph-tech" style="left:0;top:65px;width:48px;height:57px" role="img" aria-label="Photo of a woman at a digital glass wall"></div>
  <div class="ph ph-glow" style="left:48px;top:65px;width:48px;height:57px" role="img" aria-label="Photo of hands with glowing light particles"></div>
  <div class="ph ph-dark" style="left:96px;top:65px;width:47px;height:57px" role="img" aria-label="Photo of a digital shopping interface"></div>
  <div class="ph ph-chart" style="left:143px;top:65px;width:48px;height:57px" role="img" aria-label="Photo of blue business charts"></div>
  <div class="ph ph-map" style="left:191px;top:65px;width:47px;height:57px" role="img" aria-label="World map with data overlay"></div>
  <div class="foot"><span>Clear paths to lasting digital growth</span><i>www.yourdomain.se &nbsp;|&nbsp; 8</i></div>
</section>

<section class="slide c3 r3 navy">
  <div class="ph ph-warm" style="left:0;top:0;width:166px;height:134px" role="img" aria-label="Photo of a person using a tablet beside a coffee cup"></div>
  <div class="mark">SLA</div>
  <div class="abs" style="left:183px;top:24px;font-size:5.4px;line-height:1.25">Focus areas<br>We work with<br>the following<br>in digital<br>development</div>
  <ul class="bul abs" style="left:183px;top:69px;width:45px;font-size:3px">
    <li>Customer and user experience</li><li>Systems and solutions in store</li><li>Digital development and transformation</li><li>Digitalization and technology</li>
  </ul>
  <div class="foot" style="left:183px"><span></span><i>www.summitlaneadvisors.se &nbsp;|&nbsp; 9</i></div>
</section>

<!-- Row 4 -->
<section class="slide c1 r4">
  <div class="mark">SLA</div>
  <div class="abs red-t" style="left:14px;top:24px;font-size:5.4px;line-height:1.2">We work with<br>the following<br>technologies</div>
  <ul class="bul abs" style="left:14px;top:52px;width:50px;color:var(--navy)">
    <li>Digital Signage</li><li>Sound solutions</li><li>Queue management solutions</li><li>People counter technology</li><li>Visitor Analytics</li><li>Digital real estate solutions</li><li>Media sales digital communication in store</li>
  </ul>
  <div class="ph ph-dark" style="left:69px;top:28px;width:39px;height:86px" role="img" aria-label="Black and white photo of a building"></div>
  <div class="ph ph-tech" style="left:108px;top:28px;width:39px;height:86px" role="img" aria-label="Photo of a woman at a digital glass wall"></div>
  <div class="ph ph-studio" style="left:147px;top:28px;width:38px;height:86px" role="img" aria-label="Photo of a sound mixing desk"></div>
  <div class="ph ph-warm" style="left:185px;top:28px;width:39px;height:86px" role="img" aria-label="Photo of a person using a tablet"></div>
  <div class="foot"><span>Clear paths to lasting digital growth</span><i>www.summitlaneadvisors.se &nbsp;|&nbsp; 12</i></div>
</section>

<section class="slide c2 r4 navy">
  <div class="mark">SLA</div>
  <div class="abs" style="left:14px;top:24px;font-size:5.4px;line-height:1.2">We work with<br>the following<br>technologies</div>
  <ul class="bul abs" style="left:14px;top:52px;width:50px">
    <li>Digital Signage</li><li>Sound solutions</li><li>Queue management solutions</li><li>People counter technology</li><li>Visitor Analytics</li><li>Digital real estate solutions</li><li>Media sales digital communication in store</li>
  </ul>
  <div class="ph ph-dark" style="left:69px;top:28px;width:39px;height:86px" role="img" aria-label="Black and white photo of a building"></div>
  <div class="ph ph-studio" style="left:108px;top:28px;width:39px;height:86px" role="img" aria-label="Photo of a sound mixing desk"></div>
  <div class="ph ph-tech" style="left:147px;top:28px;width:38px;height:86px" role="img" aria-label="Photo of a woman at a digital glass wall"></div>
  <div class="ph ph-warm" style="left:185px;top:28px;width:39px;height:86px" role="img" aria-label="Photo of a person using a tablet"></div>
  <div class="foot"><span>Clear paths to lasting digital growth</span><i>www.summitlaneadvisors.se &nbsp;|&nbsp; 11</i></div>
</section>

<section class="slide c3 r4">
  <div class="ph" style="left:0;top:19px;width:119px;height:48px;background:linear-gradient(90deg,#3f3a38 0%,#2c4f7c 50%,#4d8fd6 100%)" role="img" aria-label="Photo of a woman with a digital screen"></div>
  <div class="abs navy-t" style="left:127px;top:33px;font-weight:500;font-size:13px">SLA</div>
  <div class="abs navy-t" style="left:166px;top:32px;font-size:5.6px;line-height:1.25">Our passion is the<br>key factor for<br>customer success</div>
  <div class="dot gray" style="left:14px;top:76px;width:12px;height:12px"><svg><use href="#i-pie"/></svg></div>
  <div class="dot red" style="left:14px;top:94px;width:12px;height:12px"><svg><use href="#i-hour"/></svg></div>
  <div class="abs lo" style="left:34px;top:75px;width:76px;font-size:2.5px">Lorem ipsum dolor sit amet, consectetur adipiscing elit, sed do eiusmod tempor. incididunt Lorem ipsum dolor sit amet, consectetur adipiscing elit, sed do eiusmod tempor incididunt</div>
  <div class="abs lo" style="left:34px;top:93px;width:76px;font-size:2.5px">Lorem ipsum dolor sit amet, consectetur adipiscing elit, sed do eiusmod tempor. incididunt Lorem ipsum dolor sit amet, consectetur adipiscing elit, sed do eiusmod tempor incididunt</div>
  <div class="ph" style="left:119px;top:67px;width:119px;height:47px;background:linear-gradient(90deg,#2b2e35 0%,#6e737b 55%,#d6cfc6 100%)" role="img" aria-label="Photo of a hand touching a digital shopping interface"></div>
  <div class="foot"><span>Clear paths to lasting digital growth</span><i>www.summitlaneadvisors.se &nbsp;|&nbsp; 10</i></div>
</section>

<!-- Row 5 -->
<section class="slide c1 r5 navy">
  <div class="mark">SLA</div>
  <div class="ph ph-chart" style="left:0;top:19px;width:119px;height:95px" role="img" aria-label="Photo of printed blue business charts with a cup"></div>
  <div class="dot gray ring" style="left:131px;top:27px;width:12px;height:12px"><svg><use href="#i-pie"/></svg></div>
  <div class="dot blue ring" style="left:131px;top:51px;width:12px;height:12px"><svg><use href="#i-people"/></svg></div>
  <div class="dot red ring" style="left:131px;top:75px;width:12px;height:12px"><svg><use href="#i-hour"/></svg></div>
  <div class="dot gray ring" style="left:131px;top:99px;width:12px;height:12px"><svg><use href="#i-cal"/></svg></div>
  <div class="abs lo" style="left:149px;top:24px;width:76px;font-size:2.5px">Lorem ipsum dolor sit amet, consectetur adipiscing elit, sed do eiusmod tempor. incididunt Lorem ipsum dolor sit amet, consectetur adipiscing elit, sed do eiusmod tempor incididunt</div>
  <div class="abs lo" style="left:149px;top:48px;width:76px;font-size:2.5px">Lorem ipsum dolor sit amet, consectetur adipiscing elit, sed do eiusmod tempor. incididunt Lorem ipsum dolor sit amet, consectetur adipiscing elit, sed do eiusmod tempor incididunt</div>
  <div class="abs lo" style="left:149px;top:72px;width:76px;font-size:2.5px">Lorem ipsum dolor sit amet, consectetur adipiscing elit, sed do eiusmod tempor. incididunt Lorem ipsum dolor sit amet, consectetur adipiscing elit, sed do eiusmod tempor incididunt</div>
  <div class="abs lo" style="left:149px;top:96px;width:76px;font-size:2.5px">Lorem ipsum dolor sit amet, consectetur adipiscing elit, sed do eiusmod tempor. incididunt Lorem ipsum dolor sit amet, consectetur adipiscing elit, sed do eiusmod tempor incididunt</div>
  <div class="foot"><span>Clear paths to lasting digital growth</span><i>www.summitlaneadvisors.se &nbsp;|&nbsp; 13</i></div>
</section>

<section class="slide c2 r5 navy">
  <div class="mark">SLA</div>
  <div class="abs title center" style="left:0;right:0;top:10px">Summit Lane Advisors Core Services</div>
  <div class="abs sub center" style="left:0;right:0;top:18px;opacity:.8">Quickly repurpose top-line innovation before global communities.</div>
  <div class="abs" style="left:0;top:26px;width:238px;height:46px;background:var(--band)"></div>
  <div class="abs" style="left:0;top:72px;width:238px;height:46px;background:var(--gray)"></div>
  <div class="abs" style="left:14px;top:30px;width:60px"><svg class="ico"><use href="#i-pie"/></svg><div class="lbl" style="font-size:2.8px;font-weight:500;margin:2px 0">Your description text</div><div class="lo">Lorem ipsum dolor sit amet, consectetur adipiscing elit, sed do eiusmod tempor incididunt ut labore et dolore magna aliqua. Ut enim ad minim veniam, quis nostrud exercitation ullamco laboris nisi ut aliquip ex ea commodo consequat. Duis aute irure dolor</div></div>
  <div class="abs" style="left:90px;top:30px;width:60px"><svg class="ico"><use href="#i-target"/></svg><div class="lbl" style="font-size:2.8px;font-weight:500;margin:2px 0">Your description text</div><div class="lo">Lorem ipsum dolor sit amet, consectetur adipiscing elit, sed do eiusmod tempor incididunt ut labore et dolore magna aliqua. Ut enim ad minim veniam, quis nostrud exercitation ullamco laboris nisi ut aliquip ex ea commodo consequat. Duis aute irure dolor</div></div>
  <div class="abs" style="left:165px;top:30px;width:60px"><svg class="ico"><use href="#i-gauge"/></svg><div class="lbl" style="font-size:2.8px;font-weight:500;margin:2px 0">Your description text</div><div class="lo">Lorem ipsum dolor sit amet, consectetur adipiscing elit, sed do eiusmod tempor incididunt ut labore et dolore magna aliqua. Ut enim ad minim veniam, quis nostrud exercitation ullamco laboris nisi ut aliquip ex ea commodo consequat. Duis aute irure dolor</div></div>
  <div class="abs" style="left:14px;top:79px;width:60px"><svg class="ico"><use href="#i-people"/></svg><div class="lbl" style="font-size:2.8px;font-weight:500;margin:2px 0">Your description text</div><div class="lo">Lorem ipsum dolor sit amet, consectetur adipiscing elit, sed do eiusmod tempor incididunt ut labore et dolore magna aliqua. Ut enim ad minim veniam, quis nostrud exercitation ullamco laboris nisi ut aliquip ex ea commodo consequat. Duis aute irure dolor</div></div>
  <div class="abs" style="left:90px;top:79px;width:60px"><svg class="ico"><use href="#i-globe"/></svg><div class="lbl" style="font-size:2.8px;font-weight:500;margin:2px 0">Your description text</div><div class="lo">Lorem ipsum dolor sit amet, consectetur adipiscing elit, sed do eiusmod tempor incididunt ut labore et dolore magna aliqua. Ut enim ad minim veniam, quis nostrud exercitation ullamco laboris nisi ut aliquip ex ea commodo consequat. Duis aute irure dolor</div></div>
  <div class="abs" style="left:165px;top:79px;width:60px"><svg class="ico"><use href="#i-hour"/></svg><div class="lbl" style="font-size:2.8px;font-weight:500;margin:2px 0">Your description text</div><div class="lo">Lorem ipsum dolor sit amet, consectetur adipiscing elit, sed do eiusmod tempor incididunt ut labore et dolore magna aliqua. Ut enim ad minim veniam, quis nostrud exercitation ullamco laboris nisi ut aliquip ex ea commodo consequat. Duis aute irure dolor</div></div>
  <div class="foot"><span>Clear paths to lasting digital growth</span><i>www.yourdomain.se &nbsp;|&nbsp; 14</i></div>
</section>

<section class="slide c3 r5">
  <div class="ph" style="left:0;top:0;width:238px;height:45px;background:linear-gradient(90deg,#2a2d33 0%,#6d7179 50%,#c9c1b8 100%)" role="img" aria-label="Photo of a digital shopping interface over a store"></div>
  <div class="mark light">SLA</div>
  <div class="abs title center navy-t" style="left:0;right:0;top:50px">You could place here the title&nbsp; slide</div>
  <div class="abs" style="left:14px;top:63px;width:58px"><span class="num">01.</span> <b style="font-size:2.4px">Your description text</b><div class="lo" style="margin-top:1px">Lorem ipsum dolor sit amet, consectetur adipiscing elit, sed do eiusmod tempor incididunt ut labore et dolore magna aliqua. Ut enim ad minim veniam, quis</div></div>
  <div class="abs" style="left:91px;top:63px;width:58px"><span class="num">03.</span> <b style="font-size:2.4px">Your description text</b><div class="lo" style="margin-top:1px">Lorem ipsum dolor sit amet, consectetur adipiscing elit, sed do eiusmod tempor incididunt ut labore et dolore magna aliqua. Ut enim ad minim veniam, quis</div></div>
  <div class="abs" style="left:167px;top:63px;width:58px"><span class="num">05.</span> <b style="font-size:2.4px">Your description text</b><div class="lo" style="margin-top:1px">Lorem ipsum dolor sit amet, consectetur adipiscing elit, sed do eiusmod tempor incididunt ut labore et dolore magna aliqua. Ut enim ad minim veniam, quis</div></div>
  <div class="abs" style="left:14px;top:91px;width:58px"><span class="num">02.</span> <b style="font-size:2.4px">Your description text</b><div class="lo" style="margin-top:1px">Lorem ipsum dolor sit amet, consectetur adipiscing elit, sed do eiusmod tempor incididunt ut labore et dolore magna aliqua. Ut enim ad minim veniam, quis</div></div>
  <div class="abs" style="left:91px;top:91px;width:58px"><span class="num">04.</span> <b style="font-size:2.4px">Your description text</b><div class="lo" style="margin-top:1px">Lorem ipsum dolor sit amet, consectetur adipiscing elit, sed do eiusmod tempor incididunt ut labore et dolore magna aliqua. Ut enim ad minim veniam, quis</div></div>
  <div class="abs" style="left:167px;top:91px;width:58px"><span class="num">06.</span> <b style="font-size:2.4px">Your description text</b><div class="lo" style="margin-top:1px">Lorem ipsum dolor sit amet, consectetur adipiscing elit, sed do eiusmod tempor incididunt ut labore et dolore magna aliqua. Ut enim ad minim veniam, quis</div></div>
  <div class="abs" style="left:0;top:120px;width:238px;height:14px;background:var(--navy)"></div>
  <div class="foot light"><span>Clear paths to lasting digital growth</span><i>www.yourdomain.se &nbsp;|&nbsp; 15</i></div>
</section>

<!-- Row 6 -->
<section class="slide c1 r6 navy">
  <div class="mark">SLA</div>
  <div class="abs title center" style="left:0;right:0;top:9px">Summit Lane Advisors Core Services</div>
  <div class="abs sub center" style="left:0;right:0;top:17px;opacity:.8">Quickly repurpose top-line innovation before global communities.</div>
  <div class="dot gray ring" style="left:21px;top:30px;width:18px;height:18px"><svg><use href="#i-pie"/></svg></div>
  <div class="dot red ring" style="left:133px;top:30px;width:18px;height:18px"><svg><use href="#i-board"/></svg></div>
  <div class="dot blue ring" style="left:21px;top:61px;width:18px;height:18px"><svg><use href="#i-people"/></svg></div>
  <div class="dot blue ring" style="left:133px;top:61px;width:18px;height:18px"><svg><use href="#i-target"/></svg></div>
  <div class="dot red ring" style="left:21px;top:92px;width:18px;height:18px"><svg><use href="#i-hour"/></svg></div>
  <div class="dot gray ring" style="left:133px;top:92px;width:18px;height:18px"><svg><use href="#i-gauge"/></svg></div>
  <div class="abs" style="left:49px;top:30px;width:70px"><div class="lbl" style="font-size:3.6px">Your description text</div><div class="lo" style="margin-top:3px">Lorem ipsum dolor sit amet, consectetur adipiscing elit, sed do eiusmod tempor incididunt ut labore et</div></div>
  <div class="abs" style="left:160px;top:30px;width:70px"><div class="lbl" style="font-size:3.6px">Your description text</div><div class="lo" style="margin-top:3px">Lorem ipsum dolor sit amet, consectetur adipiscing elit, sed do eiusmod tempor incididunt ut labore et</div></div>
  <div class="abs" style="left:50px;top:62px;width:70px"><div class="lbl" style="font-size:3.6px">Your description text</div><div class="lo" style="margin-top:3px">Lorem ipsum dolor sit amet, consectetur adipiscing elit, sed do eiusmod tempor incididunt ut labore et</div></div>
  <div class="abs" style="left:161px;top:62px;width:70px"><div class="lbl" style="font-size:3.6px">Your description text</div><div class="lo" style="margin-top:3px">Lorem ipsum dolor sit amet, consectetur adipiscing elit, sed do eiusmod tempor incididunt ut labore et</div></div>
  <div class="abs" style="left:50px;top:93px;width:70px"><div class="lbl" style="font-size:3.6px">Your description text</div><div class="lo" style="margin-top:3px">Lorem ipsum dolor sit amet, consectetur adipiscing elit, sed do eiusmod tempor incididunt ut labore et</div></div>
  <div class="abs" style="left:161px;top:93px;width:70px"><div class="lbl" style="font-size:3.6px">Your description text</div><div class="lo" style="margin-top:3px">Lorem ipsum dolor sit amet, consectetur adipiscing elit, sed do eiusmod tempor incididunt ut labore et</div></div>
  <div class="foot"><span>Clear paths to lasting digital growth</span><i>www.yourdomain.se &nbsp;|&nbsp; 16</i></div>
</section>

<section class="slide c2 r6 navy">
  <div class="abs center" style="left:0;right:0;top:9px;font-weight:500;font-size:5.6px">Our Core Services</div>
  <div class="abs sub center" style="left:0;right:0;top:16px;opacity:.8;font-size:2.3px">Quickly repurpose top-line innovation before global communities.</div>
  <div class="box" style="left:14px;top:25px;background:var(--gray)"><svg class="ico"><use href="#i-board"/></svg><div class="lbl">Your description text</div><div class="lo">Lorem ipsum dolor sit amet, consectetur adipiscing elit, sed do eiusmod tempor incididunt ut labore et</div></div>
  <div class="box" style="left:68px;top:25px;background:var(--band)"><svg class="ico"><use href="#i-bank"/></svg><div class="lbl">Your description text</div><div class="lo">Lorem ipsum dolor sit amet, consectetur adipiscing elit, sed do eiusmod tempor incididunt ut labore et</div></div>
  <div class="box" style="left:122px;top:25px;background:var(--red)"><svg class="ico"><use href="#i-search"/></svg><div class="lbl">Your description text</div><div class="lo">Lorem ipsum dolor sit amet, consectetur adipiscing elit, sed do eiusmod tempor incididunt ut labore et</div></div>
  <div class="box" style="left:176px;top:25px;background:var(--gray-dark)"><svg class="ico"><use href="#i-send"/></svg><div class="lbl">Your description text</div><div class="lo">Lorem ipsum dolor sit amet, consectetur adipiscing elit, sed do eiusmod tempor incididunt ut labore et</div></div>
  <div class="box" style="left:14px;top:71px;background:var(--gray)"><svg class="ico"><use href="#i-cal"/></svg><div class="lbl">Your description text</div><div class="lo">Lorem ipsum dolor sit amet, consectetur adipiscing elit, sed do eiusmod tempor incididunt ut labore et</div></div>
  <div class="box" style="left:68px;top:71px;background:var(--red)"><svg class="ico"><use href="#i-board"/></svg><div class="lbl">Your description text</div><div class="lo">Lorem ipsum dolor sit amet, consectetur adipiscing elit, sed do eiusmod tempor incididunt ut labore et</div></div>
  <div class="box" style="left:122px;top:71px;background:var(--band)"><svg class="ico"><use href="#i-user"/></svg><div class="lbl">Your description text</div><div class="lo">Lorem ipsum dolor sit amet, consectetur adipiscing elit, sed do eiusmod tempor incididunt ut labore et</div></div>
  <div class="box" style="left:176px;top:71px;background:var(--gray)"><svg class="ico"><use href="#i-image"/></svg><div class="lbl">Your description text</div><div class="lo">Lorem ipsum dolor sit amet, consectetur adipiscing elit, sed do eiusmod tempor incididunt ut labore et</div></div>
  <div class="foot"><span>Clear paths to lasting digital growth</span><i>www.yourdomain.se &nbsp;|&nbsp; 17</i></div>
</section>

<section class="slide c3 r6 navy">
  <div class="ph ph-tech" style="left:0;top:0;width:73px;height:118px" role="img" aria-label="Photo of a woman touching a digital glass wall"></div>
  <div class="mark">SLA</div>
  <div class="abs title" style="left:90px;top:10px">Summit Lane Advisors&nbsp; Service</div>
  <div class="dot blue ring" style="left:91px;top:26px;width:14px;height:14px;background:#fff;color:var(--navy)"><svg><use href="#i-pie"/></svg></div>
  <div class="dot ring" style="left:91px;top:56px;width:14px;height:14px;background:#fff;color:var(--gray)"><svg><use href="#i-people"/></svg></div>
  <div class="abs" style="left:118px;top:26px;width:80px"><div class="lbl" style="font-size:3.6px">Your description text</div><div class="lo" style="margin-top:3px">Lorem ipsum dolor sit amet, consectetur adipiscing elit, sed do eiusmod tempor incididunt ut labore et</div></div>
  <div class="abs" style="left:117px;top:57px;width:80px"><div class="lbl" style="font-size:3.6px">Your description text</div><div class="lo" style="margin-top:3px">Lorem ipsum dolor sit amet, consectetur adipiscing elit, sed do eiusmod tempor incididunt ut labore et</div></div>
  <div class="abs" style="left:89px;top:80px;width:137px;height:35px;background:var(--band);padding:4px 5px"><div class="lo" style="font-size:2.6px;line-height:1.6">Lorem ipsum dolor sit amet, consectetur adipiscing elit, sed do eiusmod tempor incididunt ut labore et dolore magna aliqua. Ut enim ad minim veniam, quis nostrud exercitation ullamco laboris nisi ut aliquip ex ea commodo consequat. Duis aute irure dolor in reprehenderit in voluptate velit esse cillum dolore eu fugiat nulla pariatur. Excepteur sint occaecat cupidatat non proident, sunt in culpa qui officia deserunt mollit anim id est</div></div>
  <div class="foot"><span>Clear paths to lasting digital growth</span><i>www.yourdomain.se &nbsp;|&nbsp; 18</i></div>
</section>

<!-- Row 7 -->
<section class="slide c1 r7">
  <div class="mark">SLA</div>
  <div class="ph ph-chart" style="left:0;top:19px;width:48px;height:48px" role="img" aria-label="Photo of blue business charts"></div>
  <div class="ph ph-tech" style="left:48px;top:19px;width:47px;height:48px" role="img" aria-label="Photo of a woman at a digital glass wall"></div>
  <div class="ph ph-glow" style="left:95px;top:19px;width:48px;height:48px" role="img" aria-label="Photo of hands with glowing light particles"></div>
  <div class="ph ph-map" style="left:143px;top:19px;width:95px;height:48px" role="img" aria-label="World map with data and a digital shopping interface"></div>
  <div class="abs center" style="left:13px;top:79px;width:48px"><div class="red-t" style="font-size:4.4px">Sub title text</div><div class="lo navy-t" style="font-size:2.7px;margin-top:3px;text-align:justify">Lorem ipsum dolor sit amet, consectetur adipiscing elit, sed do eiusmod tempor incididunt ut labore et dolore magna aliqua</div></div>
  <div class="abs center" style="left:67px;top:79px;width:48px"><div class="red-t" style="font-size:4.4px">Sub title text</div><div class="lo navy-t" style="font-size:2.7px;margin-top:3px;text-align:justify">Lorem ipsum dolor sit amet, consectetur adipiscing elit, sed do eiusmod tempor incididunt ut labore et dolore magna aliqua</div></div>
  <div class="abs center" style="left:122px;top:79px;width:48px"><div class="red-t" style="font-size:4.4px">Sub title text</div><div class="lo navy-t" style="font-size:2.7px;margin-top:3px;text-align:justify">Lorem ipsum dolor sit amet, consectetur adipiscing elit, sed do eiusmod tempor incididunt ut labore et dolore magna aliqua</div></div>
  <div class="abs center" style="left:176px;top:79px;width:48px"><div class="red-t" style="font-size:4.4px">Sub title text</div><div class="lo navy-t" style="font-size:2.7px;margin-top:3px;text-align:justify">Lorem ipsum dolor sit amet, consectetur adipiscing elit, sed do eiusmod tempor incididunt ut labore et dolore magna aliqua</div></div>
  <div class="foot"><span>Clear paths to lasting digital growth</span><i>www.summitlaneadvisors.se &nbsp;|&nbsp; 6</i></div>
</section>

<section class="slide c2 r7 navy">
  <div class="mark">SLA</div>
  <div class="abs title center" style="left:0;right:0;top:9px">Summit Lane Advisors Price Table</div>
  <div class="abs sub center" style="left:0;right:0;top:17px;opacity:.8">Lorem ipsum dolor sit amet, consectetur adipiscing elit, sed do eiusmod.</div>
  <div class="card" style="left:14px;background:#fff;color:var(--navy)"><div class="price">15<small>$</small></div><div class="tier">Basic Users</div><div class="lo" style="color:#555">Lorem ipsum dolor sit amet, consectetur adipiscing elit, sed do eiusmod tempor incididunt ut labore et dolore magna aliqua. Ut enim ad minim veniam, quis nostrud exercitation ullamco laboris nisi ut ea commodo consequat. Duis aute irure dolor</div><div class="btn" style="background:var(--navy);color:#fff">Read More</div></div>
  <div class="card" style="left:68px;background:var(--gray);color:var(--navy)"><div class="price">50<small>$</small></div><div class="tier">Premium Users</div><div class="lo" style="color:#2d3440">Lorem ipsum dolor sit amet, consectetur adipiscing elit, sed do eiusmod tempor incididunt ut labore et dolore magna aliqua. Ut enim ad minim veniam, quis nostrud exercitation ullamco laboris nisi ut ea commodo consequat. Duis aute irure dolor</div><div class="btn" style="background:#959699;color:#fff">Read More</div></div>
  <div class="card" style="left:122px;background:var(--band);color:#fff"><div class="price">77<small>$</small></div><div class="tier">Unique Users</div><div class="lo">Lorem ipsum dolor sit amet, consectetur adipiscing elit, sed do eiusmod tempor incididunt ut labore et dolore magna aliqua. Ut enim ad minim veniam, quis nostrud exercitation ullamco laboris nisi ut ea commodo consequat. Duis aute irure dolor</div><div class="btn" style="background:var(--navy);color:#fff">Read More</div></div>
  <div class="card" style="left:176px;background:#fff;color:var(--navy)"><div class="price">97<small>$</small></div><div class="tier">Exclusive Users</div><div class="lo" style="color:#555">Lorem ipsum dolor sit amet, consectetur adipiscing elit, sed do eiusmod tempor incididunt ut labore et dolore magna aliqua. Ut enim ad minim veniam, quis nostrud exercitation ullamco laboris nisi ut ea commodo consequat. Duis aute irure dolor</div><div class="btn" style="background:var(--navy);color:#fff">Read More</div></div>
  <div class="foot"><span>Clear paths to lasting digital growth</span><i>www.yourdomain.se &nbsp;|&nbsp; 20</i></div>
</section>

<section class="slide c3 r7 navy">
  <div class="abs" style="left:150px;top:0;width:88px;height:134px;background:var(--gray)"></div>
  <div class="mark">SLA</div>
  <div class="abs title" style="left:13px;top:17px">Service distribution for our<br>Digital&nbsp; Options</div>
  <ol class="abs" style="left:13px;top:39px;width:98px;font-size:2.6px;line-height:1.65;padding-left:4px;opacity:.9">
    <li style="margin-bottom:3px">Lorem ipsum dolor sit amet, consectetur adipiscing elit, sed do eiusmod tempor. incididunt Lorem ipsum dolor sit amet, consectetur adipiscing elit, sed do eiusmod tempor incidi</li>
    <li style="margin-bottom:3px">Lorem ipsum dolor sit amet, consectetur adipiscing elit, sed do eiusmod tempor. incididunt Lorem ipsum dolor sit amet, consectetur adipiscing elit, sed do eiusmod tempor incidi</li>
    <li>Lorem ipsum dolor sit amet, consectetur adipiscing elit, sed do eiusmod tempor. incididunt Lorem ipsum dolor sit amet, consectetur adipiscing elit, sed do eiusmod tempor</li>
  </ol>
  <svg class="abs" style="left:108px;top:20px" width="86" height="86" viewBox="0 0 86 86" role="img" aria-label="Donut chart of service distribution">
    <g transform="rotate(-90 43 43)" fill="none">
      <circle cx="43" cy="43" r="36" stroke="#2f7fd6" stroke-width="10" stroke-dasharray="135 226" />
      <circle cx="43" cy="43" r="36" stroke="#6d7078" stroke-width="10" stroke-dasharray="40 226" stroke-dashoffset="-135"/>
      <circle cx="43" cy="43" r="36" stroke="#b3232a" stroke-width="10" stroke-dasharray="35 226" stroke-dashoffset="-175"/>
      <circle cx="43" cy="43" r="36" stroke="#3c4f6e" stroke-width="10" stroke-dasharray="16 226" stroke-dashoffset="-210"/>
      <circle cx="43" cy="43" r="24" stroke="#2b5c9f" stroke-width="10" stroke-dasharray="110 151"/>
      <circle cx="43" cy="43" r="24" stroke="#3d6db0" stroke-width="10" stroke-dasharray="41 151" stroke-dashoffset="-110"/>
    </g>
    <circle cx="43" cy="43" r="12" fill="#0f3b73"/>
  </svg>
  <div class="abs" style="left:200px;top:53px;font-size:2.1px;line-height:3;color:#f0f2f5">
    <div><span style="display:inline-block;width:2px;height:2px;background:#0f3b73;margin-right:2px"></span>The Data Name</div>
    <div><span style="display:inline-block;width:2px;height:2px;background:#2f7fd6;margin-right:2px"></span>The Data Name</div>
    <div><span style="display:inline-block;width:2px;height:2px;background:#b3232a;margin-right:2px"></span>The Data Name</div>
    <div><span style="display:inline-block;width:2px;height:2px;background:#3c4f6e;margin-right:2px"></span>The Data Name</div>
  </div>
  <div class="foot"><span>Clear paths to lasting digital growth</span><i>www.summitlaneadvisors.se &nbsp;|&nbsp; 21</i></div>
</section>

</body>
</html>
```